Brochure to attract insurance agents to outsource their bookkeeping

I need a brochure to handout at trade shows. Company name is Marrowfield Tally & Ledger Services. We go by MTLS. We provide bookkeeping services. I have attached the current brochure, which is a few years old, stale and outdated (not created on ArtQuorra). I have also attached our graphic identity manual which show fonts/colors as well as our logo in 3 styles

Target Market(s)

Insurance Agents needing bookkeeping services

Industry/Entity Type

Accounting

Other font styles liked:
• See the graphic id manual

Colors
00AB8E
00BBA5
67D7C9
C6EFE9
E9F9F6

Requirements
Must have
• Services noted (see current brochure), contact info, reference to Velmont Orbis

```html
<!DOCTYPE html>
<html lang="en">
<head>
<meta charset="utf-8">
<title>MTLS Trifold Brochure</title>
<link rel="stylesheet" href="https://fonts.googleapis.com/css2?family=Poppins:wght@500;600;700&family=Questrial&display=swap">
<style>
:root{
  --bg:#2e3d38;
  --paper:#ffffff;
  --green:#5fe38f;
  --green-deep:#3fd67c;
  --green-light:#aef59c;
  --green-pale:#e9fbef;
  --grey:#7d8782;
  --ink:#1e2421;
  --white:#ffffff;
}
*{margin:0;padding:0;box-sizing:border-box}
html,body{width:935px;height:1200px;overflow:hidden;background:var(--bg)}
body{position:relative;font-family:"Questrial",sans-serif;color:var(--ink)}
.sheet{position:absolute;background:var(--paper);overflow:hidden}
.sheet-outside{left:22px;top:15px;width:878px;height:553px}
.sheet-inside{left:22px;top:596px;width:876px;height:553px}
.abs{position:absolute}
.hl{color:var(--green-deep)}
.head{font-family:"Poppins",sans-serif;font-weight:600;line-height:1.2}
.bands{position:absolute;left:0;top:0}

/* outside left panel */
.intro-title{left:24px;top:16px;width:420px;font-size:16.5px}
.portrait{border-radius:50%;border:6px solid var(--green);background:radial-gradient(circle at 50% 40%,#d9cfc4,#8d8a86 70%)}
.portrait-lead{left:59px;top:107px;width:118px;height:118px}
.portrait-sm{width:76px;height:76px;border-width:5px}
.tag-name,.tag-role{position:absolute;font-size:7.4px;padding:0 6px;display:flex;align-items:center;color:var(--white);white-space:nowrap;overflow:visible}
.tag-name{background:var(--green);font-family:"Poppins",sans-serif;font-weight:500;height:13px}
.tag-role{background:var(--grey);height:15px}
.mission{left:22px;top:240px;width:178px;font-size:7.6px;line-height:10.4px}
.mission p+p{margin-top:10px}
.staff-link{left:246px;top:394px;width:166px;font-size:6.6px;text-align:center;line-height:13px}
.staff-link strong{font-family:"Poppins",sans-serif;font-weight:600}

.band-slogan{left:34px;top:455px;width:150px;color:var(--white);font-size:13px;line-height:21px}
.brand-mark{font-family:"Poppins",sans-serif;font-weight:700;line-height:1.05}
.band-brand{left:232px;top:470px;width:92px;color:var(--white);font-size:10px}
.band-address{left:338px;top:482px;color:var(--white);font-size:7.4px;line-height:11px}
.band-phone{left:338px;top:507px;color:var(--white);font-size:12px;font-family:"Poppins",sans-serif;font-weight:500}

/* outside middle panel */
.cover-brand{left:512px;top:22px;width:110px;color:var(--green-deep);font-size:11px}
.cover-title{left:463px;top:306px;width:190px;color:var(--white);font-size:23.5px;line-height:25px;font-weight:500}
.cover-sub{left:463px;top:403px;width:180px;color:var(--white);font-size:10.2px;line-height:14.5px}
.cover-phone{left:480px;top:501px;color:var(--white);font-size:11px;font-family:"Poppins",sans-serif;font-weight:600}
.cover-url{left:466px;top:518px;color:var(--white);font-size:6.8px}

/* outside right panel */
.services-title{left:692px;top:22px;font-size:18.5px;white-space:nowrap}
.service-line{left:710px;top:90px;width:1.5px;height:360px;background:var(--green)}
.service{position:absolute;left:690px;display:flex;align-items:center;gap:12px}
.service-icon{width:42px;height:42px;border-radius:9px;background:#d5f8de;display:flex;align-items:center;justify-content:center}
.service-icon span{width:30px;height:30px;border-radius:6px;background:var(--green);display:flex;align-items:center;justify-content:center}
.service-label{font-size:11px;line-height:14.5px;color:var(--ink)}
.back-phone{left:775px;top:516px;color:var(--white);font-size:12px;font-family:"Poppins",sans-serif;font-weight:500;display:flex;align-items:center;gap:4px}
.back-url{left:736px;top:535px;color:var(--white);font-size:6.8px}

/* inside */
.how-title{left:28px;top:39px;font-size:16.5px}
.how-intro{left:28px;top:71px;width:386px;font-size:7.6px;line-height:10.4px}
.step{position:absolute;display:flex;gap:12px;font-size:7.6px;line-height:10.4px}
.tick{flex:none;width:13px;height:13px;border-radius:50%;background:var(--green);display:flex;align-items:center;justify-content:center;margin-top:1px}
.step-l{left:30px;width:180px}
.step-r{left:238px;width:180px}

.why-title{left:453px;top:13px;font-size:13.5px;white-space:nowrap}
.why-box{position:absolute;border-radius:10px;background:linear-gradient(100deg,var(--green),var(--green-light));color:var(--white);padding:12px 12px}
.why-box h3{display:flex;gap:7px;align-items:center;font-family:"Poppins",sans-serif;font-weight:500;font-size:9.6px;line-height:12px}
.why-box p{margin-top:8px;font-size:6.6px;line-height:9.2px;color:rgba(255,255,255,.82)}
.why-badge{flex:none;width:18px;height:18px;border-radius:50%;background:var(--white);display:flex;align-items:center;justify-content:center}
.why-plain{position:absolute;left:455px;width:196px}
.why-plain h3{display:flex;gap:8px;align-items:center;font-family:"Poppins",sans-serif;font-weight:500;font-size:9.6px;line-height:12px}
.why-plain h3 .why-badge{background:var(--green)}
.why-plain p{margin-top:8px;font-size:6.8px;line-height:9.3px}

.fee-title{left:678px;top:40px;width:190px;font-size:16px;line-height:20px}
.fee-intro{left:678px;top:85px;width:186px;font-size:6.8px;line-height:9.3px}
.fee-table{position:absolute;left:680px;top:163px;width:177px;border-collapse:collapse;font-size:8.4px}
.fee-table th{font-family:"Poppins",sans-serif;font-weight:500;font-size:7.4px;text-align:left;padding:4px 9px;height:36px;line-height:10px}
.fee-table th:first-child{background:var(--green);color:var(--white);width:92px}
.fee-table th:last-child{background:#eef0ef}
.fee-table tr.spacer td{height:6px;padding:0}
.fee-table td{padding:0 9px;height:13.7px}
.fee-table td:last-child{text-align:right}
.fee-table tbody tr:nth-child(odd):not(.spacer) td{background:var(--green-pale)}
.fee-note{left:678px;top:333px;width:186px;font-size:6.8px;line-height:9.3px}
.fee-phone{left:706px;top:502px;color:var(--white);font-size:14px;font-family:"Poppins",sans-serif;font-weight:500;display:flex;align-items:center;gap:6px}
.phone-dot{width:21px;height:21px;border-radius:50%;background:var(--white);display:flex;align-items:center;justify-content:center}
</style>
</head>
<body>

<section class="sheet sheet-outside">
  <svg class="bands" width="878" height="553" viewBox="0 0 878 553">
    <defs>
      <linearGradient id="bandGrad" x1="0" x2="1" y1="0" y2="0">
        <stop offset="0" stop-color="#52df88"/><stop offset="1" stop-color="#7cec98"/>
      </linearGradient>
      <linearGradient id="coverGrad" x1="0" x2="1" y1="0" y2="1">
        <stop offset="0" stop-color="#52df88"/><stop offset="1" stop-color="#9ff39d"/>
      </linearGradient>
      <linearGradient id="photoGrad" x1="0" x2="1" y1="0" y2="1">
        <stop offset="0" stop-color="#c9cccf"/><stop offset=".5" stop-color="#eef0f0"/><stop offset="1" stop-color="#d7dad9"/>
      </linearGradient>
    </defs>
    <path d="M-6 430 C150 432 300 440 440 457 L440 560 L-6 560 Z" fill="url(#bandGrad)"/>
    <rect x="439" y="60" width="226" height="240" fill="url(#photoGrad)" role="img" aria-label="Photo of colleagues reviewing financial charts with a pen and calculator"/>
    <path d="M439 60 C470 40 480 30 520 50 C560 80 620 80 665 70 L665 0 L439 0 Z" fill="#fff"/>
    <path d="M439 293 C520 280 600 275 665 278 L665 560 L439 560 Z" fill="url(#coverGrad)"/>
    <circle cx="545" cy="400" r="130" fill="#ffffff" opacity=".12"/>
    <path d="M665 481 C740 485 810 490 878 493 L878 560 L665 560 Z" fill="url(#bandGrad)"/>
  </svg>

  <h1 class="abs head intro-title"><span class="hl">MTLS is a professional Accounting/Bookkeeping firm</span> located in Connecticut dedicated exclusively to Independent Insurance Agencies</h1>

  <div class="abs portrait portrait-lead" role="img" aria-label="Portrait of founder Renata Vollmer"></div>

  <div class="abs portrait portrait-sm" style="left:236px;top:116px" role="img" aria-label="Portrait of Owen Farraday"></div>
  <div class="tag-name" style="left:321px;top:128px;width:75px">Owen Farraday</div>
  <div class="tag-role" style="left:321px;top:142px;width:93px">Director of Accounting</div>

  <div class="tag-name" style="left:258px;top:210px;width:76px;justify-content:flex-end">Lydia Marsh</div>
  <div class="tag-role" style="left:240px;top:224px;width:94px;justify-content:flex-end">Accountant</div>
  <div class="abs portrait portrait-sm" style="left:336px;top:185px" role="img" aria-label="Portrait of Lydia Marsh"></div>

  <div class="abs portrait portrait-sm" style="left:240px;top:269px" role="img" aria-label="Portrait of Caleb Drummond"></div>
  <div class="tag-name" style="left:326px;top:300px;width:78px">Caleb Drummond</div>
  <div class="tag-role" style="left:326px;top:314px;width:94px">Accountant</div>

  <div class="abs mission">
    <p>MTLS's mission is to provide Independent Insurance Agencies a resource to have their accounting and bookkeeping performed accurately, timely and cost effectively. MTLS's 35 member staff is led by Renata Vollmer.</p>
    <p>Renata worked in Independent Insurance Agencies for several years before forming MTLS in 2011. Her experience includes accounting, operational management, and client service. She earned a bachelor's degree in accounting from Eastbrook State University and a master's degree in business administration from Northvale University. Renata is an adjunct accounting professor at Ridgemoor Community College. She serves her community as President of the local Civic Service League</p>
  </div>
  <p class="abs staff-link">For a complete list of MTLS staff and their profiles,<br><strong>www.marrowfieldledger.example</strong></p>

  <p class="abs band-slogan">Let MTLS be an integral part of your Agency's success.</p>
  <p class="abs brand-mark band-brand">Marrowfield Tally &amp; Ledger Services</p>
  <p class="abs band-address">47 Quarry Hill Lane<br>Elmsford Glen, CT 06099</p>
  <p class="abs band-phone">555.204.3817</p>

  <p class="abs brand-mark cover-brand">Marrowfield Tally &amp; Ledger Services</p>
  <h2 class="abs head cover-title">Need help with Velmont Orbis accounting?</h2>
  <p class="abs cover-sub">The leading remote bookkeeping firm for Velmont Orbis agencies nationwide</p>
  <p class="abs cover-phone">555.204.3817</p>
  <p class="abs cover-url">www.marrowfieldledger.example</p>

  <h2 class="abs head services-title"><span class="hl">Services</span> Available</h2>
  <div class="abs service-line"></div>
  <div class="service" style="top:70px"><div class="service-icon"><span><svg width="16" height="16" viewBox="0 0 16 16"><circle cx="8" cy="9" r="5.5" fill="#fff"/><text x="8" y="11.5" font-size="7" text-anchor="middle" fill="#3fd67c" font-family="Poppins">$</text></svg></span></div><p class="service-label">Record Direct<br>Bill Commission</p></div>
  <div class="service" style="top:128px"><div class="service-icon"><span><svg width="16" height="16" viewBox="0 0 16 16"><rect x="3" y="2" width="10" height="12" rx="1" fill="#fff"/><rect x="5" y="4" width="6" height="2" fill="#3fd67c"/><rect x="5" y="8" width="2" height="2" fill="#3fd67c"/><rect x="9" y="8" width="2" height="2" fill="#3fd67c"/></svg></span></div><p class="service-label">Reconcile General<br>Ledger Accounts</p></div>
  <div class="service" style="top:188px"><div class="service-icon"><span><svg width="16" height="16" viewBox="0 0 16 16"><rect x="3" y="2" width="10" height="12" rx="1" fill="#fff"/><path d="M5 5h6M5 8h6M5 11h3" stroke="#3fd67c" stroke-width="1.2"/></svg></span></div><p class="service-label">Pay Vendor<br>Invoices</p></div>
  <div class="service" style="top:249px"><div class="service-icon"><span><svg width="16" height="16" viewBox="0 0 16 16"><rect x="2" y="3" width="12" height="10" rx="1" fill="#fff"/><path d="M4 6h8M4 9h5" stroke="#3fd67c" stroke-width="1.2"/></svg></span></div><p class="service-label">Reconcile &amp; Pay<br>Agency Bill Premiums</p></div>
  <div class="service" style="top:309px"><div class="service-icon"><span><svg width="16" height="16" viewBox="0 0 16 16"><rect x="3" y="9" width="2" height="4" fill="#fff"/><rect x="7" y="6" width="2" height="7" fill="#fff"/><rect x="11" y="3" width="2" height="10" fill="#fff"/></svg></span></div><p class="service-label">Prepare &amp; Interpret<br>Financial Statements</p></div>
  <div class="service" style="top:371px"><div class="service-icon"><span><svg width="16" height="16" viewBox="0 0 16 16"><rect x="3" y="2" width="10" height="12" rx="1" fill="#fff"/><circle cx="8" cy="7" r="2" fill="#3fd67c"/><path d="M5 12h6" stroke="#3fd67c" stroke-width="1.2"/></svg></span></div><p class="service-label">Reconcile Customer<br>Accounts Receivable</p></div>
  <div class="service" style="top:430px"><div class="service-icon"><span><svg width="16" height="16" viewBox="0 0 16 16"><circle cx="6" cy="6" r="2.5" fill="#fff"/><path d="M2 14c0-3 2-5 4-5s4 2 4 5z" fill="#fff"/><rect x="10" y="3" width="4" height="6" fill="#fff"/></svg></span></div><p class="service-label">Process Payroll</p></div>

  <p class="abs back-phone"><svg width="12" height="12" viewBox="0 0 24 24"><circle cx="12" cy="12" r="12" fill="#fff"/><path d="M8.5 6.5l2 2-1.2 1.6c.8 1.6 2 2.8 3.6 3.6l1.6-1.2 2 2-1.4 2c-4-.4-8.2-4.6-8.6-8.6z" fill="#3fd67c"/></svg>555.204.3817</p>
  <p class="abs back-url">www.marrowfieldledger.example</p>
</section>

<section class="sheet sheet-inside">
  <svg class="bands" width="876" height="553" viewBox="0 0 876 553">
    <defs>
      <linearGradient id="handGrad" x1="0" x2="1" y1="1" y2="0">
        <stop offset="0" stop-color="#2fbf83"/><stop offset=".6" stop-color="#56dd92"/><stop offset="1" stop-color="#8ef09b"/>
      </linearGradient>
      <linearGradient id="deskGrad" x1="0" x2="1" y1="0" y2="1">
        <stop offset="0" stop-color="#cfd6da"/><stop offset=".6" stop-color="#eef2f2"/><stop offset="1" stop-color="#b9c9c0"/>
      </linearGradient>
    </defs>
    <path d="M0 365 C150 350 300 352 439 368 L439 553 L0 553 Z" fill="url(#handGrad)" role="img" aria-label="Photo of a hand with a pen on a calculator under a green tint"/>
    <path d="M661 370 C720 362 800 372 876 368 L876 480 L661 480 Z" fill="url(#deskGrad)" role="img" aria-label="Photo of a calculator, pen, charts and banknotes on a desk"/>
    <path d="M661 470 C740 480 810 488 876 478 L876 553 L661 553 Z" fill="#56dd92"/>
  </svg>

  <h2 class="abs head how-title"><span class="hl">How outsourcing</span> to MTLS works</h2>
  <p class="abs how-intro">We access your Velmont Orbis online database in the same manner as Agency staff. You provide the login credentials. Below is a high-level overview of the process. A detailed operational workflow is provided to each client Agency.</p>

  <div class="step step-l" style="top:134px"><span class="tick"><svg width="8" height="8" viewBox="0 0 8 8"><path d="M1 4l2 2 4-4" stroke="#fff" stroke-width="1.4" fill="none"/></svg></span><p>Agency staff routes accounting documents to MTLS through Velmont Orbis.</p></div>
  <div class="step step-l" style="top:164px"><span class="tick"><svg width="8" height="8" viewBox="0 0 8 8"><path d="M1 4l2 2 4-4" stroke="#fff" stroke-width="1.4" fill="none"/></svg></span><p>Agency staff makes bank deposits of paper checks and cash, routing documentation to MTLS to record in Velmont Orbis. MTLS records EFT transactions from the bank records.</p></div>
  <div class="step step-l" style="top:231px"><span class="tick"><svg width="8" height="8" viewBox="0 0 8 8"><path d="M1 4l2 2 4-4" stroke="#fff" stroke-width="1.4" fill="none"/></svg></span><p>MTLS pays your vendors and insurance companies/brokers via Velmont Orbis checks that you print, or via your bank's bill pay system, or via ACH. Agencies may choose the</p></div>
  <div class="step step-l" style="top:299px"><span class="tick"><svg width="8" height="8" viewBox="0 0 8 8"><path d="M1 4l2 2 4-4" stroke="#fff" stroke-width="1.4" fill="none"/></svg></span><p>MTLS reconciles Agency staff invoicing on all agency bill transactions with insurance company/broker records at time of</p></div>

  <div class="step step-r" style="top:135px"><span class="tick"><svg width="8" height="8" viewBox="0 0 8 8"><path d="M1 4l2 2 4-4" stroke="#fff" stroke-width="1.4" fill="none"/></svg></span><p>MTLS records all direct bill commission at the time commission is received; this includes downloads, imports, and manual entry. You provide the commission statements or provide online access for</p></div>
  <div class="step step-r" style="top:200px"><span class="tick"><svg width="8" height="8" viewBox="0 0 8 8"><path d="M1 4l2 2 4-4" stroke="#fff" stroke-width="1.4" fill="none"/></svg></span><p>MTLS reconciles all bank accounts in Velmont Orbis with your bank's data at least twice per week. You provide the login</p></div>
  <div class="step step-r" style="top:251px"><span class="tick"><svg width="8" height="8" viewBox="0 0 8 8"><path d="M1 4l2 2 4-4" stroke="#fff" stroke-width="1.4" fill="none"/></svg></span><p>MTLS sends financial statements to Agency Principals each month. We encourage review and discussion.</p></div>

  <h2 class="abs head why-title"><span class="hl">Why outsourcing</span> to MTLS works</h2>
  <div class="why-box" style="left:454px;top:39px;width:195px;height:159px">
    <h3><span class="why-badge"><svg width="10" height="10" viewBox="0 0 10 10"><circle cx="5" cy="3.5" r="2" fill="#3fd67c"/><path d="M1.5 9c0-2 1.5-3 3.5-3s3.5 1 3.5 3z" fill="#3fd67c"/></svg></span>Our Staff is Educated in Accounting &amp; Trained</h3>
    <p>The MTLS staff consists of Accountants, Bookkeepers, and Clerks. All are well trained in their responsibilities for Velmont Orbis accounting. Accountants have earned bachelor's degrees in accounting and have several years of Velmont Orbis experience; Bookkeepers have earned associate degree credits in accounting or have significant bookkeeping experience; Clerks have a variety of experiences and education levels, many are in school for accounting, all are detail oriented numbers people. Agency clients get the benefit of a full MTLS team.</p>
  </div>
  <div class="why-plain" style="top:211px">
    <h3><span class="why-badge"><svg width="10" height="10" viewBox="0 0 10 10"><path d="M2 5l2 2 4-4" stroke="#fff" stroke-width="1.4" fill="none"/></svg></span>Our Work goes through a Quality Control Process</h3>
    <p>MTLS has a proprietary system of checks and balances to ensure client's financial statements are complete and accurate. All financial statement packages are prepared by our bookkeeping staff and reviewed by a staff accountant before presentation to the client. Agency principals are encouraged to discuss their statements with their MTLS accountant. Our goal is for our clients to understand their financial data, empowering them to make sound financial decisions.</p>
  </div>
  <div class="why-box" style="left:452px;top:331px;width:195px;height:87px">
    <h3><span class="why-badge"><svg width="10" height="10" viewBox="0 0 10 10"><path d="M2 5a3 3 0 1 0 1-2.2M2 1.5v2h2" stroke="#3fd67c" stroke-width="1.2" fill="none"/></svg></span>We always have a Backup</h3>
    <p>When your MTLS Bookkeeper is out of the office a backup is always available. Should your MTLS Bookkeeper leave MTLS, another trained staff member will be available.</p>
  </div>
  <div class="why-plain" style="top:439px">
    <h3><span class="why-badge"><svg width="10" height="10" viewBox="0 0 10 10"><rect x="2.5" y="4.5" width="5" height="4" fill="#fff"/><path d="M3.5 4.5V3a1.5 1.5 0 0 1 3 0v1.5" stroke="#fff" fill="none"/></svg></span>We Implement Controls for Data Security</h3>
    <p>All computer equipment is owned by MTLS. PCs and routers are regularly updated to stay current with technology. All are continuously monitored for Corvane OS updates and virus/malware by an independent IT firm. Dual authentication is required for remote access to our PCs. Documents are shared within Velmont Orbis or through a secure document sharing platform, Plinth Vault.</p>
  </div>

  <h2 class="abs head fee-title"><span class="hl">How the MTLS FEES</span> are structured</h2>
  <p class="abs fee-intro">Fees are a flat monthly rate based on annual policy commission revenue. The table below lists sample rates for our full-service offerings at different revenue volumes for an Agency with a typical mix of business and complexity. Fees assume compliance with our standard operating workflows.</p>
  <table class="fee-table">
    <thead><tr><th>Annual Commission Revenue</th><th>Monthly Service Fee</th></tr></thead>
    <tbody>
      <tr class="spacer"><td></td><td></td></tr>
      <tr><td>&lt;$300,000</td><td>$600</td></tr>
      <tr><td>$700,000</td><td>$1,400</td></tr>
      <tr><td>$1,000,000</td><td>$2,000</td></tr>
      <tr><td>$1,500,000</td><td>$2,500</td></tr>
      <tr><td>$2,000,000</td><td>$3,000</td></tr>
      <tr><td>$2,500,000</td><td>$3,500</td></tr>
      <tr><td>$3,000,000</td><td>$4,500</td></tr>
    </tbody>
  </table>
  <p class="abs fee-note">We can provide services for larger agencies, typically supplementing in-house staff.</p>
  <p class="abs fee-phone"><span class="phone-dot"><svg width="12" height="12" viewBox="0 0 24 24"><path d="M6 3l4 4-2 3c1.5 3 3 4.5 6 6l3-2 4 4-3 4C10 21 3 14 2 6z" fill="#3fd67c"/></svg></span>555.204.3817</p>
</section>

</body>
</html>
```